Helping Seniors and their families start the discussion about driver safety, and explore options to preserve senior independence.
Target Market(s)
Seniors and their families
Industry/Entity Type
Non Profit
Number of Pages Required
4 page
Font styles to use
Sans Serif
Requirements
Must have
- Logo
- Application for Amber Crossings Registration

Nice to have
- Colorful, and designed for Senior Citizens and their Families

```html
<!DOCTYPE html>
<html lang="en">
<head>
<meta charset="utf-8">
<title>Amber Crossings — Senior Transportation</title>
<link rel="stylesheet" href="https://fonts.googleapis.com/css2?family=Montserrat:wght@400;500;600;700&family=Open+Sans:ital,wght@0,400;0,600;1,400&display=swap">
<style>
:root{
  --green:#0b7a4a;
  --green-dark:#075234;
  --green-mid:#0a6b42;
  --yellow:#f2aa00;
  --orange:#eea00c;
  --ink:#333;
  --muted:#666;
  --rule:#e2e2e2;
  --footer:#ececec;
  --white:#fff;
}
*{box-sizing:border-box;margin:0;padding:0}
html,body{width:1200px;height:3114px;overflow:hidden}
body{font-family:"Open Sans",Arial,sans-serif;color:var(--ink);background:var(--white);position:relative}

/* header */
.site-header{position:absolute;left:0;top:0;width:1200px;height:108px;background:var(--white)}
.brand{position:absolute;display:flex;align-items:center;gap:12px}
.brand-name{font-family:"Montserrat",Arial,sans-serif;font-weight:700;color:var(--green);line-height:1}
.brand-mark{border-radius:50%;background:var(--green)}
.site-header .brand{left:112px;top:28px}
.site-header .brand-name{font-size:30px;width:150px}
.site-header .brand-mark{width:40px;height:40px}
.main-nav{position:absolute;left:383px;top:52px;display:flex;gap:33px;font-family:"Montserrat",Arial,sans-serif;font-size:16px;color:var(--ink)}
.main-nav .active{color:var(--green)}
.nav-dot{position:absolute;left:392px;top:24px;width:26px;height:26px;border:2px solid #bbb;border-radius:50%}
.header-phone{position:absolute;left:938px;top:46px;font-family:"Montserrat",Arial,sans-serif;font-size:20px;color:var(--ink);display:flex;align-items:center;gap:8px}

/* hero */
.hero{position:absolute;left:0;top:108px;width:1200px;height:525px;background:linear-gradient(90deg,#3e3a35 0%,#8b8f86 35%,#6f8a55 62%,#4f7a33 100%)}
.hero-caption{position:absolute;left:125px;top:245px;width:455px;height:114px;background:rgba(40,40,40,.55);color:var(--white);font-family:"Montserrat",Arial,sans-serif;font-size:33px;line-height:40px;padding:18px 16px}
.slider-dots{position:absolute;display:flex;gap:8px}
.slider-dots span{width:14px;height:14px;border-radius:50%;background:var(--white)}
.hero .slider-dots{left:556px;top:483px}

/* why */
.why{position:absolute;left:0;top:633px;width:1200px;height:457px}
.why h2{position:absolute;left:129px;top:86px;font-family:"Montserrat",Arial,sans-serif;font-weight:500;font-size:31px;color:#222}
.why p{position:absolute;left:131px;top:138px;width:570px;font-size:12.5px;line-height:24px;color:var(--muted)}
.btn-call{position:absolute;left:133px;top:330px;width:151px;height:42px;background:var(--orange);color:var(--white);font-family:"Montserrat",Arial,sans-serif;font-size:14px;display:flex;align-items:center;justify-content:center;border-radius:3px}
.portrait{position:absolute;left:721px;top:35px;width:356px;height:356px;border-radius:50%;border:10px solid #e6e6e6;background:radial-gradient(circle at 50% 40%,#b89a82,#5b5147 70%,#3a3a38)}

/* policies */
.policies{position:absolute;left:0;top:1090px;width:1200px;height:390px;background:linear-gradient(180deg,var(--green-mid),var(--green-dark))}
.policy{position:absolute;top:80px;width:280px;color:var(--white)}
.policy svg{display:block;height:66px}
.policy h3{font-family:"Montserrat",Arial,sans-serif;font-weight:500;font-size:20px;margin-top:22px}
.policy p{font-size:11.5px;line-height:21px;margin-top:10px;opacity:.92}
.btn-outline{display:inline-flex;align-items:center;justify-content:center;width:110px;height:34px;border:2px solid var(--white);font-size:12px;margin-top:20px;font-family:"Montserrat",Arial,sans-serif}
.policy-divider{position:absolute;top:100px;width:1px;height:236px;background:rgba(255,255,255,.3)}

/* destinations */
.destinations{position:absolute;left:0;top:1480px;width:1200px;height:384px;background:var(--yellow);color:var(--white)}
.destinations h2{position:absolute;left:0;top:52px;width:1200px;text-align:center;font-family:"Montserrat",Arial,sans-serif;font-weight:600;font-size:25px;line-height:34px}
.dest-list{position:absolute;top:160px;list-style:none;font-family:"Montserrat",Arial,sans-serif;font-size:12.5px;font-weight:500}
.dest-list li{height:33.5px;padding-left:16px;position:relative}
.dest-list li::before{content:"";position:absolute;left:0;top:4px;border-left:7px solid var(--white);border-top:5px solid transparent;border-bottom:5px solid transparent}

/* on the go */
.on-the-go{position:absolute;left:0;top:1864px;width:1200px;height:488px;background:linear-gradient(90deg,#7d6a4c 0%,#c9b48a 35%,#f2ecdc 55%,#e8dcc0 75%,#b8a27a 100%)}
.go-text{position:absolute;left:640px;top:86px;width:470px}
.go-text h2{font-family:"Montserrat",Arial,sans-serif;font-weight:400;font-size:33px;color:#222}
.go-text h3{font-family:"Montserrat",Arial,sans-serif;font-weight:400;font-size:24px;color:#222;margin-top:2px}
.go-text p{font-size:13px;line-height:27px;color:#444;margin-top:16px}
.btn-green{display:inline-flex;align-items:center;justify-content:center;width:139px;height:35px;background:var(--green);color:var(--white);font-family:"Montserrat",Arial,sans-serif;font-size:13px;margin-top:22px}

/* testimonials */
.testimonials{position:absolute;left:0;top:2352px;width:1200px;height:384px}
.testimonials h2{position:absolute;left:0;top:56px;width:1200px;text-align:center;font-family:"Montserrat",Arial,sans-serif;font-weight:500;font-size:25px;color:var(--green)}
.avatar{position:absolute;top:133px;width:100px;height:100px;border-radius:50%;background:radial-gradient(circle at 50% 40%,#d9c2b0,#8a7668 70%,#5a5048)}
.quote-card{position:absolute;top:120px;width:305px;height:167px;border:2px solid var(--rule);border-radius:4px;padding:22px 22px 20px 26px;font-style:italic;font-size:13px;line-height:23px;color:#444;background:var(--white)}
.quote-card::before{content:"";position:absolute;left:-12px;top:50px;width:20px;height:20px;background:var(--white);border-left:2px solid var(--rule);border-bottom:2px solid var(--rule);transform:rotate(45deg)}
.quote-card .author{font-style:normal;font-size:12.5px;margin-top:6px}
.testimonials .slider-dots{left:578px;top:315px}
.testimonials .slider-dots span{width:12px;height:12px;background:#999}
.testimonials .slider-dots span:first-child{background:var(--white);border:2px solid #999}

/* footer */
.site-footer{position:absolute;left:0;top:2736px;width:1200px;height:316px;background:var(--footer)}
.site-footer .brand{left:120px;top:68px}
.site-footer .brand-name{font-size:36px;width:180px}
.site-footer .brand-mark{width:48px;height:48px}
.foot-col{position:absolute;top:52px;font-size:13px;color:#555;line-height:25px}
.foot-col h4{font-family:"Montserrat",Arial,sans-serif;font-weight:500;font-size:17px;color:#222;margin-bottom:10px}
.foot-col ul{list-style:none}
.foot-col .register-link{color:var(--green);font-weight:600}
.contact-row{display:flex;gap:10px;align-items:flex-start}
.contact-row svg{flex:none;margin-top:5px}
.partner-badge{width:150px;height:46px;background:#cfcfcf;border-radius:4px;margin-top:6px}
.social{display:flex;gap:10px;margin-top:12px}
.social span{width:32px;height:32px;border-radius:50%;background:var(--green)}
.copyright{position:absolute;left:0;top:3052px;width:1200px;height:62px;background:var(--footer);border-top:1px solid #ddd;text-align:center;font-size:12px;color:#888;line-height:62px}
</style>
</head>
<body>

<header class="site-header">
  <div class="brand"><span class="brand-name">Amber Crossings</span><span class="brand-mark"></span></div>
  <span class="nav-dot"></span>
  <nav class="main-nav">
    <span class="active">Home</span><span>About Us</span><span>Services</span><span>Why Us</span><span>Review</span><span>Contact</span>
  </nav>
  <div class="header-phone">
    <svg width="18" height="18" viewBox="0 0 24 24"><path fill="#0b7a4a" d="M6.6 10.8a15 15 0 0 0 6.6 6.6l2.2-2.2c.3-.3.7-.4 1-.2 1.1.4 2.3.6 3.6.6.6 0 1 .4 1 1V20c0 .6-.4 1-1 1A17 17 0 0 1 3 4c0-.6.4-1 1-1h3.5c.6 0 1 .4 1 1 0 1.3.2 2.5.6 3.6.1.3 0 .7-.2 1z"/></svg>
    (555)-014-2290
  </div>
</header>

<section class="hero" role="img" aria-label="Smiling senior man driving a car, green trees outside the window">
  <div class="hero-caption">Schedule Transportation at Time and Safe</div>
  <div class="slider-dots"><span></span><span></span><span></span><span></span></div>
</section>

<section class="why">
  <h2>Why Amber Crossings?</h2>
  <p>Convenience With Amber Crossings, you can schedule transportation at a time that is convenient for you, eliminating the need to work around the schedule of family and friends. Transportation is not limited to medical appointments. You can travel to the mall, concerts, church, grocery store, theater, etc.<br>&nbsp;Go when and where you want to go! Specialized Services Our team is experienced in providing services to seniors and individuals with physical and cognitive issues such as blindness, cancer, hip/knee replacement, Autism, Alzheimer's, loss of hearing, OCD, etc.</p>
  <div class="btn-call">CALL US NOW</div>
  <div class="portrait" role="img" aria-label="Smiling senior woman seated in a car"></div>
</section>

<section class="policies">
  <div class="policy" style="left:156px">
    <svg width="66" viewBox="0 0 66 66" fill="none" stroke="#fff" stroke-width="3"><rect x="3" y="10" width="54" height="48" rx="3"/><line x1="3" y1="22" x2="57" y2="22"/><line x1="16" y1="4" x2="16" y2="14"/><line x1="44" y1="4" x2="44" y2="14"/><g stroke-width="2"><line x1="12" y1="32" x2="20" y2="32"/><line x1="26" y1="32" x2="34" y2="32"/><line x1="12" y1="42" x2="20" y2="42"/><line x1="26" y1="42" x2="34" y2="42"/></g><circle cx="50" cy="50" r="13" fill="#0a6b42"/><polyline points="50,43 50,50 55,53"/></svg>
    <h3>Schedule Changes</h3>
    <p>If there is a change in either the pickup or drop off location, please give Amber Crossings 24 hours' notice with the new address</p>
    <span class="btn-outline">Read More</span>
  </div>
  <div class="policy-divider" style="left:440px"></div>
  <div class="policy" style="left:482px">
    <svg width="66" viewBox="0 0 66 66" fill="none" stroke="#fff" stroke-width="3"><circle cx="33" cy="33" r="30"/><line x1="12" y1="54" x2="54" y2="12"/></svg>
    <h3>Cancellation</h3>
    <p>We understand unexpected situations arise that require a change in plans. Our cancellation policy is very simple.</p>
    <span class="btn-outline">Read More</span>
  </div>
  <div class="policy-divider" style="left:768px"></div>
  <div class="policy" style="left:812px">
    <svg width="110" viewBox="0 0 110 66"><path fill="#fff" d="M4 44c0-6 3-9 10-10l16-3 14-10c4-3 8-4 14-4h18c6 0 10 2 14 6l8 8c6 1 10 4 10 9v6c0 2-1 3-3 3h-9a10 10 0 0 0-20 0H36a10 10 0 0 0-20 0H7c-2 0-3-1-3-3zM48 24l-8 8h22V21h-8c-2 0-4 1-6 3zm18-3v11h22l-7-7c-2-3-5-4-8-4z"/><circle cx="26" cy="51" r="7" fill="#fff"/><circle cx="83" cy="51" r="7" fill="#fff"/></svg>
    <h3>Return Pickup</h3>
    <p>If our driver arrives for return pickup and the client is not ready and requests pickup at a later time, a return pickup fee of $20.00 is charged.</p>
    <span class="btn-outline">Read More</span>
  </div>
</section>

<section class="destinations">
  <h2>Go When and Where you Want to Go<br>with Amber Crossings!</h2>
  <ul class="dest-list" style="left:125px">
    <li>Medical Appointment</li><li>Dental Appointment</li><li>Outpatient Testing and Procedures</li><li>Physical Threapy</li><li>Barber/Beauty Shop Appointments</li>
  </ul>
  <ul class="dest-list" style="left:461px">
    <li>Dialysis Clinic</li><li>Radiation Clinics</li><li>Church Events</li><li>Senior Centres/Adult Care Center</li><li>Hospital/Nursing Home Discharge</li>
  </ul>
  <ul class="dest-list" style="left:768px">
    <li>Airport Transportation</li><li>Special Family Events</li><li>Grocery Shopping and Other Type of Shopping</li><li>Bank and Post Office Errands</li>
  </ul>
</section>

<section class="on-the-go" role="img" aria-label="Senior couple waving from a silver car beside a sunlit golden field">
  <div class="go-text">
    <h2>Senior on the Go</h2>
    <h3>Keeping Us Safe</h3>
    <p>We follow you from location to location, and then follow up with you to see how the ride was and if you have questions or concerns. Understanding Your Needs We understand that everyone is not alike, therefore, needs are not alike. It is important to us that our services meet your needs. Before scheduling service</p>
    <span class="btn-green">READ MORE</span>
  </div>
</section>

<section class="testimonials">
  <h2>What Peoples Says About Us</h2>
  <div class="avatar" style="left:154px" role="img" aria-label="Portrait of a senior client"></div>
  <div class="quote-card" style="left:270px">“Curabitur tristique mi condimentum orci Phasellus pellentesque aliquam enim Proin dui lectus cursus eu mattis laoreet viverra sit amet”<div class="author">By Author Name</div></div>
  <div class="avatar" style="left:616px" role="img" aria-label="Portrait of a senior client"></div>
  <div class="quote-card" style="left:731px">“Curabitur tristique mi condimentum orci Phasellus pellentesque aliquam enim Proin dui lectus cursus eu mattis laoreet viverra sit amet”<div class="author">By Author Name</div></div>
  <div class="slider-dots"><span></span><span></span><span></span></div>
</section>

<footer class="site-footer">
  <div class="brand"><span class="brand-name">Amber Crossings</span><span class="brand-mark"></span></div>
  <div class="foot-col" style="left:397px">
    <h4>Quick Links</h4>
    <ul><li>Home</li><li>About Us</li><li>Why Us</li><li>Our Services</li><li>Contact Us</li><li class="register-link">Registration Application</li></ul>
  </div>
  <div class="foot-col" style="left:579px;width:260px">
    <h4>Contact Us</h4>
    <div class="contact-row"><svg width="12" height="16" viewBox="0 0 12 16"><path fill="#0b7a4a" d="M6 0a6 6 0 0 0-6 6c0 4.5 6 10 6 10s6-5.5 6-10a6 6 0 0 0-6-6zm0 8.5A2.5 2.5 0 1 1 6 3.5a2.5 2.5 0 0 1 0 5z"/></svg><span>412 Meadowlark Lane Suite<br>210 Fairbrook, Georgia 30999</span></div>
    <div class="contact-row"><svg width="14" height="14" viewBox="0 0 24 24"><path fill="#0b7a4a" d="M6.6 10.8a15 15 0 0 0 6.6 6.6l2.2-2.2c.3-.3.7-.4 1-.2 1.1.4 2.3.6 3.6.6.6 0 1 .4 1 1V20c0 .6-.4 1-1 1A17 17 0 0 1 3 4c0-.6.4-1 1-1h3.5c.6 0 1 .4 1 1 0 1.3.2 2.5.6 3.6.1.3 0 .7-.2 1z"/></svg><span>555-014-2290</span></div>
    <div class="contact-row"><svg width="14" height="14" viewBox="0 0 14 14"><rect x="1" y="3" width="12" height="10" fill="#0b7a4a"/><rect x="3" y="1" width="8" height="4" fill="#0b7a4a"/><rect x="3" y="6" width="8" height="3" fill="#fff"/></svg><span>555-017-3364</span></div>
    <div class="partner-badge"></div>
  </div>
  <div class="foot-col" style="left:872px;width:230px">
    <h4>Hours &amp; Timing</h4>
    <p>Mon-Fri: 9 am - 6 pm (office)<br>Rides offered 24 hours a day 7 days a week based on availability</p>
    <div class="social"><span></span><span></span><span></span><span></span></div>
  </div>
</footer>
<div class="copyright">© 2017 Company Name All right reserved &nbsp;Term of Use</div>

</body>
</html>
```